Combat Sports news website design

Redesigning our existing website to make it more modern, responsive and suitable for our needs. The design needs to take in to account all aspects of our current website structure and services. View the existing website at https://www.bramblewire.co.nz

Particular attention should be paid to our livestream service, which is growing and needs to be much more user friendly to the current experience.

The homepage, article listings and article pages need designs.

Target Market(s)

Combat sports fans

Industry/Entity Type

Media

Coding

Coded - Design and coding required

Number of Pages Required

5+ page

Font styles to use
Sans Serif

Requirements
Must have
• All the functionality of the existing website must be taken in to account, and improved upon.
New design must incorporate our existing logo/colour scheme as this has only just been designed.

```html
<!DOCTYPE html>
<html lang="en">
<head>
<meta charset="utf-8">
<title>Bramble Wire – Combat Sports News</title>
<link href="https://fonts.googleapis.com/css2?family=Poppins:wght@400;500;600;700;800&display=swap" rel="stylesheet">
<style>
:root{
  --red:#c3161f;
  --red-dark:#98111a;
  --ink:#1c1d20;
  --nav:#1b1c1f;
  --panel:#26272b;
  --grey-bg:#ecedef;
  --text:#333;
  --muted:#777;
  --line:#dcdcdc;
  --white:#fff;
}
*{box-sizing:border-box;margin:0;padding:0}
html,body{width:1200px;height:4120px;overflow:hidden}
body{font-family:"Poppins",Arial,sans-serif;color:var(--text);background:var(--white);font-size:12px;line-height:1.45}
a{color:inherit;text-decoration:none}
ul{list-style:none}

.site-header{height:120px;display:flex;align-items:center;justify-content:space-between;padding:0 64px;background:var(--white)}
.search{width:170px;height:28px;border:1px solid #bbb;display:flex;align-items:center;justify-content:space-between;padding:0 8px;font-size:11px;color:#999}
.brand{display:flex;align-items:center;gap:8px;font-weight:800;font-size:26px;color:var(--ink);letter-spacing:1px}
.brand-mark{width:22px;height:22px;background:var(--red)}
.account{display:flex;gap:8px}
.btn-pill{font-size:10px;font-weight:600;color:var(--white);background:var(--ink);padding:6px 16px;border-radius:14px}
.btn-pill.red{background:var(--red)}

.main-nav{height:48px;background:var(--nav);display:flex;padding-left:72px}
.main-nav a{color:var(--white);font-size:12px;font-weight:500;padding:0 24px;display:flex;align-items:center;text-transform:uppercase}
.main-nav a.active{background:#4a4b50}

.hero{position:relative;height:592px;background:radial-gradient(ellipse at 25% 55%,#7a4a36 0%,#3a2520 35%,#16110f 70%),#111;}
.hero-text{position:absolute;left:0;right:0;top:315px;text-align:center;color:var(--white)}
.hero-title{font-size:46px;font-weight:800;letter-spacing:1px}
.hero-sub{font-size:13px;font-weight:600;margin-top:6px;line-height:1.3}
.btn-red{display:inline-block;background:var(--red);color:var(--white);font-weight:600;font-size:12px;padding:9px 26px;border-radius:20px;margin-top:16px}
.dots{position:absolute;bottom:30px;left:0;right:0;display:flex;justify-content:center;gap:8px}
.dots span{width:8px;height:8px;border-radius:50%;background:#777}
.dots span.on{background:var(--white)}

.headlines-band{background:var(--grey-bg);padding:40px 72px;height:580px}
.card-box{background:var(--white);padding:28px 32px;height:500px}
.section-head{display:flex;justify-content:space-between;align-items:center;margin-bottom:22px}
.section-title{font-size:28px;font-weight:800;color:var(--ink);text-transform:uppercase}
.arrows{display:flex;gap:4px}
.arrows span{width:22px;height:22px;background:var(--ink);color:var(--white);font-size:12px;display:flex;align-items:center;justify-content:center}
.arrows span.red{background:var(--red)}
.news-grid{display:grid;grid-template-columns:repeat(3,1fr);gap:24px}
.thumb{display:block;width:100%}
.meta{font-size:10px;color:var(--muted);margin:10px 0 6px;display:flex;gap:14px}
.news-title{font-size:13px;font-weight:700;color:var(--ink);line-height:1.35}
.excerpt{font-size:10.5px;color:#666;margin:6px 0 10px}
.read-more{font-size:10.5px;color:var(--ink);text-decoration:underline}

.video-band{background:linear-gradient(#222327,#2d2e33);padding:60px 72px;height:660px;display:flex;gap:20px}
.video-card{background:var(--white);padding:24px;width:688px;height:540px}
.video-frame{position:relative;height:432px;background:linear-gradient(135deg,#3b2c4a,#1d1b2b 60%,#4a2a22)}
.play{position:absolute;left:50%;top:50%;transform:translate(-50%,-50%)}
.video-side{flex:1;background:#1b1c1f;height:540px;padding:16px}
.tabs{display:flex;margin-bottom:12px}
.tabs span{flex:1;text-align:center;font-size:10px;font-weight:600;color:var(--white);padding:7px 0;background:#3a3b40}
.tabs span.on{background:var(--red)}
.side-list li{display:flex;gap:12px;padding:10px 0;border-bottom:1px solid #333}
.side-list .mini{width:80px;height:60px;flex:none;background:linear-gradient(135deg,#5a3d33,#231c1c)}
.side-list .date{font-size:9.5px;color:#aaa}
.side-list .t{font-size:11px;color:var(--white);font-weight:500;line-height:1.35}

.earlier{display:flex;gap:24px;padding:60px 72px 0;height:1180px}
.earlier-main{width:690px}
.list-item{display:flex;gap:20px;border:1px solid var(--line);padding:12px;margin-bottom:16px;height:250px}
.list-item .thumb{width:220px;height:224px;flex:none}
.list-item .excerpt{font-size:11px}
.aside{flex:1}
.aside-head{background:var(--red-dark);color:var(--white);font-size:22px;font-weight:800;padding:12px 16px;text-transform:uppercase}
.event{border:1px solid var(--line);border-top:none;padding:12px}
.event .thumb{height:190px}
.event p{font-size:12px;font-weight:700;color:var(--ink);margin-top:8px}
.poll{border:1px solid var(--line);border-top:none;padding:14px 16px}
.poll h4{font-size:11px;font-weight:600;margin-bottom:8px}
.poll label{display:flex;align-items:center;gap:8px;font-size:11px;margin-bottom:5px}
.poll label i{width:10px;height:10px;border:1px solid #888;border-radius:50%}
.poll-actions{display:flex;justify-content:space-between;margin-top:10px}

.newsletter{text-align:center;padding:140px 0 0;height:420px}
.newsletter h2{font-size:26px;font-weight:800;color:var(--ink)}
.newsletter p{font-size:10px;color:var(--muted);letter-spacing:1px}
.subscribe{display:inline-flex;gap:10px;margin-top:20px;align-items:center}
.subscribe span.field{width:300px;height:34px;border:1px solid #bbb;border-radius:18px;text-align:left;padding:8px 16px;font-size:11px;color:#999}

.site-footer{background:var(--nav);height:480px;padding:60px 72px;display:grid;grid-template-columns:330px 180px 180px 1fr;gap:40px;color:#ccc}
.site-footer .brand{color:var(--white);font-size:24px}
.about{font-size:11px;margin:14px 0 18px}
.contact-line{display:flex;align-items:center;gap:10px;margin-bottom:12px;font-size:12px;color:var(--white)}
.icon-dot{width:30px;height:30px;border-radius:50%;background:var(--red);display:flex;align-items:center;justify-content:center}
.foot-title{font-size:15px;font-weight:700;color:var(--white);margin-bottom:14px;text-transform:uppercase}
.foot-links li{font-size:11px;margin-bottom:6px}
.foot-links li::before{content:"› ";color:var(--red)}
.form-field{background:var(--white);height:26px;margin-bottom:8px;font-size:10px;color:#999;padding:5px 8px}
.form-field.tall{height:70px}
.bottom-bar{height:40px;background:var(--red-dark);display:flex;align-items:center;justify-content:space-between;padding:0 72px;color:var(--white);font-size:11px}
.socials{display:flex;gap:6px}
.socials i{width:20px;height:20px;border-radius:50%;background:var(--nav)}
</style>
</head>
<body>

<header class="site-header">
  <div class="search"><span>Search</span>
    <svg width="12" height="12" viewBox="0 0 12 12"><circle cx="5" cy="5" r="3.8" fill="none" stroke="#555" stroke-width="1.4"/><line x1="8" y1="8" x2="11" y2="11" stroke="#555" stroke-width="1.4"/></svg>
  </div>
  <a class="brand" href="https://www.bramblewire.co.nz"><span class="brand-mark"></span>BRAMBLE WIRE</a>
  <div class="account"><a class="btn-pill" href="#">LOGIN</a><a class="btn-pill red" href="#">REGISTER</a></div>
</header>

<nav class="main-nav">
  <a class="active" href="#">Home</a><a href="#">About Us</a><a href="#">Sports ▾</a><a href="#">Live Events</a><a href="#">Video</a><a href="#">Upcoming Event</a><a href="#">Contact Us</a><a href="#">Advertise</a>
</nav>

<section class="hero" role="img" aria-label="Two boxers facing off for the headline pay-per-view bout">
  <div class="hero-text">
    <div class="hero-title">MARSH VS CALDER</div>
    <div class="hero-sub">LIVE ON<br>PAY-PER-VIEW</div>
    <a class="btn-red" href="#">LIVE VIEW HERE</a>
  </div>
  <div class="dots"><span class="on"></span><span></span><span></span></div>
</section>

<section class="headlines-band">
  <div class="card-box">
    <div class="section-head"><h2 class="section-title">Latest Headlines</h2><div class="arrows"><span class="red">‹</span><span>›</span></div></div>
    <div class="news-grid">
      <article>
        <div class="thumb" style="height:160px;background:linear-gradient(135deg,#6a4a3c,#2a1f1c)" role="img" aria-label="Fight night promo photo"></div>
        <div class="meta"><span>26 Mar, 2021</span><span>Boxing</span></div>
        <h3 class="news-title">Friday Night Fights to hit streaming tonight</h3>
        <p class="excerpt">Friday Night Fights is back with a strong card tonight, headed by two local title bouts and a packed undercard for fans at home.</p>
        <a class="read-more" href="#">Read More</a>
      </article>
      <article>
        <div class="thumb" style="height:160px;background:linear-gradient(135deg,#5a4538,#1e1a18)" role="img" aria-label="Two boxers exchanging punches in the ring"></div>
        <div class="meta"><span>27 Apr, 2021</span><span>Boxing</span></div>
        <h3 class="news-title">Rico Hale aims to stay busy in 2021</h3>
        <p class="excerpt">Rico Hale is a front running contender in the middleweight division and hopes to fight three times before the year ends.</p>
        <a class="read-more" href="#">Read More</a>
      </article>
      <article>
        <div class="thumb" style="height:160px;background:linear-gradient(135deg,#8a3b2e,#2a1b18)" role="img" aria-label="Weigh-in poster for the main event"></div>
        <div class="meta"><span>27 Apr, 2021</span><span>MMA</span></div>
        <h3 class="news-title">VIDEO: Reyes vs Kahu weigh-in highlights</h3>
        <p class="excerpt">The weigh-in is complete for both fighters ahead of a headline bout that has sold out the arena within days of release.</p>
        <a class="read-more" href="#">Read More</a>
      </article>
    </div>
  </div>
</section>

<section class="video-band">
  <div class="video-card">
    <div class="section-head"><h2 class="section-title">Video</h2><div class="arrows"><span class="red">‹</span><span>›</span></div></div>
    <div class="video-frame" role="img" aria-label="Wrestling show promo video still">
      <svg class="play" width="64" height="64" viewBox="0 0 64 64"><circle cx="32" cy="32" r="30" fill="#c3161f"/><path d="M25 19 L47 32 L25 45 Z" fill="#fff"/></svg>
    </div>
  </div>
  <aside class="video-side">
    <div class="tabs"><span class="on">HEADLINES</span><span>TRENDING</span></div>
    <ul class="side-list">
      <li><div class="mini" role="img" aria-label="Fighter thumbnail"></div><div><div class="date">10:02am, Tue 27 Apr 2021</div><div class="t">Apex Wrestling stars return to the ring on Saturday</div></div></li>
      <li><div class="mini" role="img" aria-label="Fighter thumbnail"></div><div><div class="date">2:02pm, Tue 27 Apr 2021</div><div class="t">VIDEO – "I'm bringing pain" – Dane Ruru declares war on Manu Tipene</div></div></li>
      <li><div class="mini" role="img" aria-label="Fighter thumbnail"></div><div><div class="date">1:38am, Tue 27 Apr 2021</div><div class="t">VIDEO – "I'm bringing pain" – Dane Ruru declares war on Manu Tipene</div></div></li>
      <li><div class="mini" role="img" aria-label="Fighter thumbnail"></div><div><div class="date">2:02pm, Tue 27 Apr 2021</div><div class="t">VIDEO – "I'm bringing pain" – Dane Ruru declares war on Manu Tipene</div></div></li>
      <li><div class="mini" role="img" aria-label="Fighter thumbnail"></div><div><div class="date">3:45pm, Mon 26 Apr 2021</div><div class="t">VIDEO – "I'm bringing pain" – Dane Ruru declares war on Manu Tipene</div></div></li>
      <li><div class="mini" role="img" aria-label="Fighter thumbnail"></div><div><div class="date">2:02pm, Mon 26 Apr 2021</div><div class="t">VIDEO – "I'm bringing pain" – Dane Ruru declares war on Manu Tipene</div></div></li>
    </ul>
  </aside>
</section>

<section class="earlier">
  <div class="earlier-main">
    <div class="section-head"><h2 class="section-title">Earlier News</h2></div>
    <article class="list-item">
      <div class="thumb" style="background:linear-gradient(135deg,#4a6a8a,#1f2a38)" role="img" aria-label="Kickboxers in the ring"></div>
      <div><div class="meta"><span>26 Apr, 2021</span></div>
      <h3 class="news-title">Three new New Zealand champions were crowned at the Fight Night last Saturday in Hamilton</h3>
      <p class="excerpt">The 14-fight event culminated in a bout that saw local favourite Tane Kahu retain his belt, and a new super lightweight champion named after a close decision.</p>
      <a class="read-more" href="#">Read More</a></div>
    </article>
    <article class="list-item">
      <div class="thumb" style="background:linear-gradient(135deg,#6a4a3a,#2a1e1a)" role="img" aria-label="Champion holding title belt"></div>
      <div><div class="meta"><span>26 Apr, 2021</span></div>
      <h3 class="news-title">South Island star says 'I'm ready' for the title fight in Auckland</h3>
      <p class="excerpt">In the ring tonight, the heavyweight champion will complete preparations for his first defence against a dangerous opponent from overseas.</p>
      <a class="read-more" href="#">Read More</a></div>
    </article>
    <article class="list-item">
      <div class="thumb" style="background:linear-gradient(135deg,#8a7a6a,#2a2a2a)" role="img" aria-label="Referee raising fighter's hand"></div>
      <div><div class="meta"><span>26 Apr, 2021</span></div>
      <h3 class="news-title">New Zealand's lone flyweight wins title defence on points</h3>
      <p class="excerpt">The 25 year old has been training for 11 years and says the belt is only the beginning of a much bigger plan.</p>
      <a class="read-more" href="#">Read More</a></div>
    </article>
    <article class="list-item">
      <div class="thumb" style="background:linear-gradient(135deg,#7a5a46,#2a1e18)" role="img" aria-label="Fighter posing shirtless"></div>
      <div><div class="meta"><span>26 Apr, 2021</span></div>
      <h3 class="news-title">South Island fighter returns with a convincing stoppage win</h3>
      <p class="excerpt">The fighter was competitive, but finished strongly in the third round with a body shot that dropped his opponent.</p>
      <a class="read-more" href="#">Read More</a></div>
    </article>
  </div>
  <aside class="aside">
    <div class="aside-head">Upcoming Events</div>
    <div class="event"><div class="thumb" style="background:linear-gradient(135deg,#5a6a7a,#1e2228)" role="img" aria-label="Fighters in training"></div><p>Silas Reed claims debut win against Otis Vane</p></div>
    <div class="event"><div class="thumb" style="background:linear-gradient(135deg,#9a6a3a,#2a1a14)" role="img" aria-label="Championship belt on display"></div><p>Explosive card for Apex Wrestling's next PPV</p></div>
    <div class="event"><div class="thumb" style="background:linear-gradient(135deg,#6a3a6a,#1e1628)" role="img" aria-label="Wrestler on stage under lights"></div><p>The Iron Five definitely would be the biggest force</p></div>
    <div class="aside-head" style="margin-top:16px;font-size:18px">Opinion Poll</div>
    <div class="poll">
      <h4>What combat sport do you prefer?</h4>
      <label><i></i>MMA</label><label><i></i>Wrestling</label><label><i></i>Kickboxing</label><label><i></i>Muay Thai</label><label><i></i>All of the above</label>
      <div class="poll-actions"><a class="btn-pill" href="#">Vote</a><a class="btn-pill red" href="#">View Results</a></div>
    </div>
  </aside>
</section>

<section class="newsletter">
  <h2>SUBSCRIBE OUR NEWSLETTER</h2>
  <p>SIGN UP FOR EXCLUSIVE OFFERS AND LATEST NEWS</p>
  <div class="subscribe"><span class="field">Enter Your Email</span><a class="btn-pill red" href="#">Subscribe Now</a></div>
</section>

<footer class="site-footer">
  <div>
    <div class="brand"><span class="brand-mark"></span>BRAMBLE WIRE</div>
    <p class="about">Lorem ipsum is simply dummy text used as a placeholder to show how the layout reads before the final copy is written.</p>
    <div class="contact-line"><span class="icon-dot"><svg width="14" height="14" viewBox="0 0 14 14"><path d="M3 1 L5 1 L6 4 L4.5 5.2 Q5.5 7.8 8.8 9.5 L10 8 L13 9 L13 11 Q13 13 11 13 Q1 12 1 3 Q1 1 3 1Z" fill="#fff"/></svg></span>1-800-123-1234</div>
    <div class="contact-line"><span class="icon-dot"><svg width="14" height="12" viewBox="0 0 14 12"><rect x="1" y="1" width="12" height="10" fill="none" stroke="#fff" stroke-width="1.4"/><path d="M1 1 L7 7 L13 1" fill="none" stroke="#fff" stroke-width="1.4"/></svg></span>newsdesk@bramblewire.co.nz</div>
  </div>
  <div><h4 class="foot-title">Quick Links</h4><ul class="foot-links"><li>Home</li><li>About Us</li><li>Live Events</li><li>Contact Us</li><li>Login</li><li>Register</li><li>Advertise</li></ul></div>
  <div><h4 class="foot-title">Sports</h4><ul class="foot-links"><li>MMA</li><li>Kickboxing</li><li>Boxing</li><li>Wrestling</li><li>Pro Cage</li><li>Summit FC</li></ul></div>
  <div><h4 class="foot-title">Get In Touch</h4>
    <div class="form-field">Name*</div><div class="form-field">Email*</div><div class="form-field tall">Message</div>
    <a class="btn-pill red" href="#" style="display:inline-block;margin-left:90px">SEND</a>
  </div>
</footer>
<div class="bottom-bar">
  <span>Copyright ©2021 Bramble Wire Media Ltd &nbsp;|&nbsp; Site Terms &nbsp;|&nbsp; Privacy &nbsp;|&nbsp; Advertise &nbsp;|&nbsp; Contact Us</span>
  <div class="socials"><i></i><i></i><i></i><i></i></div>
</div>

</body>
</html>
```